Tidewalk Intro Course QM Dive Bonaire

QM Dive is looking for a great flyer to promote our Tidewalk Intro Course around Bonaire, the Caribbean.

Bonaire is shore dive capital of the world.
Our guests rent a pick-up truck. we would like to inform them about the possibilities of the Tidewalk Intro Dive.

We have the logo, images and text available. Its the catchy and mind blowing design we are looking for to create an eye-catch flyer.
One side will be in English, the other side will be in Dutch.

Target Market(s)

Visitors (non divers) of the island Bonaire

Industry/Entity Type

Diving industry

Font styles to use
Sans Serif

Colors
0094D4
00A9DD
6FCCEA
C7EBF8
E9F6FB
F0912C
F2A743
F7CA91
FBE8D2
FDF5EE

Requirements
Must have
• The picture with the car and divers next to it is mandatory. Inspire to go for a tidewalk intro dive, show the beauty under water, easy to come dive with us, just takes half a day
Should not have
• Should not have pictures taken not around Bonaire.

```html
<!DOCTYPE html>
<html lang="en">
<head>
<meta charset="utf-8">
<title>Tidewalk Intro Course – QM Dive Bonaire</title>
<link rel="stylesheet" href="https://fonts.googleapis.com/css2?family=Barlow+Condensed:ital,wght@1,800&family=Open+Sans:wght@400;700;800&display=swap">
<style>
  :root{
    --stage:#8c8c8c;
    --navy:#2b3a6c;
    --navy-deep:#22305c;
    --blue:#0094D4;
    --blue-mid:#00A9DD;
    --blue-light:#6FCCEA;
    --blue-pale:#C7EBF8;
    --blue-mist:#E9F6FB;
    --orange:#F0912C;
    --orange-soft:#F2A743;
    --white:#ffffff;
  }
  *{box-sizing:border-box;margin:0;padding:0}
  html,body{width:1200px;height:2504px;overflow:hidden}
  body{background:var(--stage);font-family:"Open Sans",Arial,sans-serif;position:relative}

  .flyer{position:absolute;left:112px;width:976px;height:1190px;background:var(--blue-mist);overflow:hidden;box-shadow:0 6px 18px rgba(0,0,0,.35)}
  .flyer--en{top:32px}
  .flyer--nl{top:1282px}

  .hero-photo{position:absolute;left:0;top:0;width:976px;height:440px;
    background:linear-gradient(180deg,#cfe3ea 0%,#e9e4d6 40%,#d9cdb4 70%,#c8b999 100%)}
  .waves{position:absolute;left:0;top:0;width:976px;height:1190px}

  .brand{position:absolute;left:34px;top:30px;display:flex;align-items:center;gap:12px;
    background:var(--white);padding:14px 20px;border-radius:6px}
  .brand__mark{width:30px;height:30px;background:var(--orange)}
  .brand__name{font-family:"Open Sans",Arial,sans-serif;font-weight:800;font-size:34px;color:var(--blue)}

  .shot{position:absolute;border-radius:50%;border:6px solid var(--white)}
  .shot--reef{left:548px;top:228px;width:140px;height:140px;background:radial-gradient(circle at 40% 40%,#4fb3d9,#0d5f8c)}
  .shot--divers{left:690px;top:186px;width:226px;height:226px;background:linear-gradient(180deg,#9fd3e6 0%,#5aa7c4 45%,#d8c9a8 100%)}

  .title{position:absolute;left:20px;right:20px;top:452px;height:64px;text-align:center;white-space:nowrap;
    font-family:"Barlow Condensed",Arial,sans-serif;font-style:italic;font-weight:800;
    font-size:60px;line-height:64px;color:var(--orange);letter-spacing:.5px}
  .title--long{font-size:48px}
  .intro{position:absolute;left:120px;right:120px;top:530px;text-align:center;color:var(--white);font-size:18px;line-height:1.5}

  .passion{position:absolute;left:60px;top:640px;font-size:24px;font-weight:800;color:var(--orange)}
  .passion-list{position:absolute;left:60px;top:678px;width:700px;list-style:none;color:var(--white);font-size:15px;line-height:1.55}
  .passion-list li::before{content:"– "}

  .badge{position:absolute;left:820px;top:730px;width:104px;height:104px;border-radius:10px;background:var(--white);display:flex;align-items:center;justify-content:center}
  .badge__shape{width:64px;height:64px;border-radius:50%;background:var(--navy)}

  .paradise{position:absolute;left:60px;top:930px;font-size:24px;font-weight:800;color:var(--navy)}
  .paradise-text{position:absolute;left:60px;right:60px;top:966px;font-size:15px;line-height:1.55;color:var(--navy)}

  .cta{position:absolute;left:60px;right:60px;top:1076px;font-size:20px;font-weight:800;line-height:1.35;color:var(--orange);text-transform:uppercase}
</style>
</head>
<body>

<section class="flyer flyer--en">
  <div class="hero-photo" role="img" aria-label="Scuba gear and tank resting on a white sandy Bonaire beach"></div>
  <svg class="waves" viewBox="0 0 976 1190" aria-hidden="true">
    <path d="M0 380 C220 330 420 410 640 380 C800 360 900 340 976 330 V470 H0Z" fill="var(--blue-light)"/>
    <path d="M0 410 C230 360 430 440 650 405 C810 385 910 372 976 365 V880 C760 930 520 860 300 900 C160 925 60 915 0 905Z" fill="var(--navy)"/>
    <path d="M0 905 C60 915 160 925 300 900 C520 860 760 930 976 880 V1190 H0Z" fill="var(--blue-pale)"/>
    <path d="M0 1050 C260 1020 520 1080 976 1040 V1190 H0Z" fill="var(--blue-mist)"/>
  </svg>

  <div class="brand"><span class="brand__mark"></span><span class="brand__name">QM Dive</span></div>
  <div class="shot shot--reef" role="img" aria-label="Colourful coral reef underwater"></div>
  <div class="shot shot--divers" role="img" aria-label="Two divers in wetsuits standing next to the pick-up truck"></div>

  <h1 class="title">Tidewalk Intro Course on Bonaire</h1>
  <p class="intro">Fall in love with diving in our underwater paradise. Under the guidance of a dive instructor you will learn the basic skills for peaceful diving in a fun and easy way.</p>

  <h2 class="passion">DEVELOP A PASSION FOR MARINE LIFE</h2>
  <ul class="passion-list">
    <li>Ages 10 and up can sign up for our intro dive</li>
    <li>You'll dive straight into the water after a brief theoretic introduction</li>
    <li>The Tidewalk Intro Course will take 3–4 hours</li>
    <li>Before participating, you are required to fill out a medical questionnaire</li>
    <li>A group consists of a maximum of 4 people</li>
    <li>Experience the splendor of the ocean without much distraction by other divers</li>
    <li>And enjoy a lot of personal attention given by your instructor</li>
  </ul>
  <div class="badge" role="img" aria-label="Certification badge"><span class="badge__shape"></span></div>

  <h2 class="paradise">UNDERWATER PARADISE</h2>
  <p class="paradise-text">Bonaire is the place to learn how to scuba dive. After a brief introduction we will directly dive into the sea, where the reef starts in shallow waters. We know the perfect dive sites for beginners. Here the sea bed slopes gradually down and you'll be amazed by the most beautiful fish and corals.</p>

  <p class="cta">Stop by at our front office and we are happy to answer all your questions or to book your 'Tidewalk Intro Dive'!</p>
</section>

<section class="flyer flyer--nl">
  <div class="hero-photo" role="img" aria-label="Duikuitrusting en fles op een wit zandstrand op Bonaire"></div>
  <svg class="waves" viewBox="0 0 976 1190" aria-hidden="true">
    <path d="M0 380 C220 330 420 410 640 380 C800 360 900 340 976 330 V470 H0Z" fill="var(--blue-light)"/>
    <path d="M0 410 C230 360 430 440 650 405 C810 385 910 372 976 365 V880 C760 930 520 860 300 900 C160 925 60 915 0 905Z" fill="var(--navy)"/>
    <path d="M0 905 C60 915 160 925 300 900 C520 860 760 930 976 880 V1190 H0Z" fill="var(--blue-pale)"/>
    <path d="M0 1050 C260 1020 520 1080 976 1040 V1190 H0Z" fill="var(--blue-mist)"/>
  </svg>

  <div class="brand"><span class="brand__mark"></span><span class="brand__name">QM Dive</span></div>
  <div class="shot shot--reef" role="img" aria-label="Kleurrijk koraalrif onder water"></div>
  <div class="shot shot--divers" role="img" aria-label="Twee duikers in duikpak naast de pick-up truck"></div>

  <h1 class="title title--long">Proefduik op Bonaire (Tidewalk Intro Course)</h1>
  <p class="intro">Word verliefd op het geweld van duiken in onze onderwaterparadijs. Onder begeleiding van een duikinstructeur ontdek je op een makkelijke en leuke manier alle basisvaardigheden voor een heerlijke duik.</p>

  <h2 class="passion">LIEFDE VOOR HET WATERLEVEN</h2>
  <ul class="passion-list">
    <li>Onze proefduik is voor iedereen vanaf 10 jaar</li>
    <li>Na een korte theoretische introductie gaat je meteen het water in</li>
    <li>De activiteit duurt 3 tot 4 uur</li>
    <li>Je vult vooraf een korte medische vragenlijst in om veilig te duiken</li>
    <li>Een groep bestaat uit maximaal 4 personen</li>
    <li>Geniet van de pracht van de oceaan zonder afleiding van anderen</li>
    <li>En heel veel persoonlijke aandacht van je duikinstructeur</li>
  </ul>
  <div class="badge" role="img" aria-label="Certificeringsbadge"><span class="badge__shape"></span></div>

  <h2 class="paradise">ONDERWATERPARADIJS</h2>
  <p class="paradise-text">Bonaire is bij uitstek de plek voor een proefduik. Na een korte introductie duiken we direct de zee in waar het rif al vrij snel begint. Bonaire kent veel ideale duikplekken voor beginners. Hier loopt de zeebodem langzaam af en word je verrast door de mooiste vissen en koralen.</p>

  <p class="cta">Kom gerust langs bij onze front office, wij zijn graag bereid je vragen te beantwoorden of om de 'Tidewalk Intro Dive' in te plannen.</p>
</section>

</body>
</html>
```